Young, modern, highly skilled carpenter needs business card design

I need a business card design for my construction business. Its called 'Pemberton Building Partners'. Im looking for a ultra modern design that incorporates P B P, the first letters of the name with only a subtle reference to carpentry. The design should reflect my high quality work and eye for detail. i have also uploaded some exmaple designs i like.

Industry/Entity Type

Construction

Requirements
Must have
• Name of business, my name, mobile number, ABN number, email address
Nice to have
• A logo incorporating the name of the business

```html
<!DOCTYPE html>
<html lang="en">
<head>
<meta charset="utf-8">
<title>Pemberton Building Partners – Business Card Concepts</title>
<link rel="stylesheet" href="https://fonts.googleapis.com/css2?family=Roboto+Condensed:wght@700&family=Open+Sans:wght@400;600;700&family=Tinos&display=swap">
<style>
  :root {
    --brand-blue: #1b6ea6;
    --accent-red: #e0262a;
    --paper: #ffffff;
    --ink: #111111;
    --shadow: #3a3a3a;
    --card-edge: #9a9a9a;
  }
  * { box-sizing: border-box; margin: 0; padding: 0; }
  html, body { width: 927px; height: 1200px; overflow: hidden; background: var(--paper); }
  .sheet { position: relative; width: 927px; height: 1200px; }

  .wordmark {
    position: absolute;
    font-family: "Roboto Condensed", Arial Narrow, sans-serif;
    font-weight: 700;
    color: var(--brand-blue);
    white-space: nowrap;
    line-height: 1;
  }
  .wordmark--reverse { color: var(--paper); }
  .mark-dot { position: absolute; border-radius: 50%; background: var(--accent-red); }

  .label {
    position: absolute;
    font-family: "Tinos", "Times New Roman", serif;
    font-size: 17px;
    color: var(--ink);
  }

  .card {
    position: absolute;
    width: 386px;
    height: 213px;
    overflow: hidden;
    box-shadow: 9px 9px 4px var(--shadow);
  }
  .card--blue { background: var(--brand-blue); }
  .card--white { background: var(--paper); border: 1px solid var(--card-edge); }

  .card__disc { position: absolute; border-radius: 50%; }
  .card__disc--white { background: var(--paper); }
  .card__disc--blue { background: var(--brand-blue); }

  .company-name {
    position: absolute;
    font-family: "Roboto Condensed", Arial Narrow, sans-serif;
    font-weight: 700;
    white-space: nowrap;
    color: var(--brand-blue);
  }
  .company-name--reverse { color: var(--paper); }

  .web {
    position: absolute;
    font-family: "Open Sans", Arial, sans-serif;
    font-weight: 600;
    font-size: 10.5px;
    color: var(--accent-red);
  }

  .contact {
    position: absolute;
    font-family: "Open Sans", Arial, sans-serif;
    font-size: 9.6px;
    line-height: 13.2px;
    color: var(--brand-blue);
  }
  .contact--reverse { color: var(--paper); }
  .contact__name { font-weight: 600; font-size: 12.5px; line-height: 15px; }
  .contact__role { margin-bottom: 13px; }
  .contact__address { margin-bottom: 8px; }
  .contact__row { display: flex; }
  .contact__row dt { font-weight: 700; width: 56px; }
  .contact__row dd { font-weight: 600; }
  .contact__email { margin-top: 9px; }

  .divider { position: absolute; width: 1px; background: var(--ink); }
</style>
</head>
<body>
<main class="sheet">

  <!-- Logo concepts -->
  <div class="wordmark" style="left:156px; top:110px; font-size:98px;">P B P</div>
  <span class="mark-dot" style="left:368px; top:178px; width:18px; height:18px;"></span>

  <div class="wordmark" style="left:548px; top:118px; font-size:60px;">P B P</div>
  <span class="mark-dot" style="left:680px; top:158px; width:12px; height:12px;"></span>
  <div class="company-name" style="left:510px; top:200px; font-size:17.5px;">Pemberton Building Partners</div>

  <!-- Front A -->
  <p class="label" style="left:45px; top:270px;">Front</p>
  <section class="card card--blue" style="left:45px; top:301px;">
    <div class="card__disc card__disc--white" style="left:270px; top:-23px; width:240px; height:240px;"></div>
    <div class="wordmark wordmark--reverse" style="left:74px; top:58px; font-size:46px;">P B P</div>
    <div class="company-name company-name--reverse" style="left:35px; top:117px; font-size:13.5px;">Pemberton Building Partners</div>
  </section>

  <!-- Front B -->
  <p class="label" style="left:473px; top:279px;">Front</p>
  <section class="card card--blue" style="left:474px; top:311px;">
    <div class="wordmark wordmark--reverse" style="left:118px; top:52px; font-size:52px;">P B P</div>
    <div class="company-name company-name--reverse" style="left:60px; top:118px; font-size:16px;">Pemberton Building Partners</div>
  </section>

  <!-- Back A -->
  <p class="label" style="left:280px; top:582px;">Back</p>
  <section class="card card--white" style="left:273px; top:605px;">
    <div class="wordmark" style="left:60px; top:70px; font-size:40px;">P B P</div>
    <div class="company-name" style="left:12px; top:117px; font-size:11px;">Pemberton Building Partners</div>
    <div class="web" style="left:70px; top:176px;">www. pbp.co.au</div>
    <div class="divider" style="left:210px; top:26px; height:170px;"></div>
    <div class="contact" style="left:234px; top:20px;">
      <p class="contact__name">Daniel Whitmore</p>
      <p class="contact__role">Contractor</p>
      <p class="contact__address">4/218 Kestrel Avenue<br>Ferndale QLD 4013<br>Ferndale Central QLD 4015</p>
      <dl>
        <div class="contact__row"><dt>ABN No :</dt><dd>048372915</dd></div>
        <div class="contact__row"><dt>Phone:</dt><dd>07 3185 2290</dd></div>
        <div class="contact__row"><dt>Fax :</dt><dd>07 3185 2291</dd></div>
        <div class="contact__row"><dt>Mobile :</dt><dd>0412557308</dd></div>
      </dl>
      <p class="contact__email">danielwhitmore@pbp.co.au</p>
    </div>
  </section>

  <!-- Front C -->
  <p class="label" style="left:73px; top:850px;">Front</p>
  <section class="card card--white" style="left:55px; top:885px;">
    <div class="card__disc card__disc--blue" style="left:270px; top:-20px; width:240px; height:240px;"></div>
    <div class="wordmark" style="left:72px; top:54px; font-size:46px;">P B P</div>
    <div class="company-name" style="left:33px; top:112px; font-size:13.5px;">Pemberton Building Partners</div>
    <div class="web" style="left:87px; top:176px;">www. pbp.co.au</div>
  </section>

  <!-- Back B -->
  <p class="label" style="left:499px; top:857px;">Back</p>
  <section class="card card--blue" style="left:487px; top:885px;">
    <div class="card__disc card__disc--white" style="left:265px; top:-20px; width:240px; height:240px;"></div>
    <div class="contact contact--reverse" style="left:34px; top:20px;">
      <p class="contact__name">Daniel Whitmore</p>
      <p class="contact__role">Contractor</p>
      <p class="contact__address">4/218 Kestrel Avenue<br>Ferndale QLD 4013<br>Ferndale Central QLD 4015</p>
      <dl>
        <div class="contact__row"><dt>ABN No :</dt><dd>048372915</dd></div>
        <div class="contact__row"><dt>Phone:</dt><dd>07 3185 2290</dd></div>
        <div class="contact__row"><dt>Fax :</dt><dd>07 3185 2291</dd></div>
        <div class="contact__row"><dt>Mobile :</dt><dd>0412557308</dd></div>
      </dl>
      <p class="contact__email">danielwhitmore@pbp.co.au</p>
    </div>
  </section>

</main>
</body>
</html>
```